update company powerpoint deck - inject more power/personality into the deck

We would like a designer to provide us with a powerpoint template based on our brand guidelines. Current brand guidelines, colours and existing deck provided.
Current deck lacks punch. We really like our black and white elements - but need options for graphs, tables and charts. We potentially need more supplementary colours to what is currently in our brand guidelines.

Target Market(s)

listed companies - B2B. We are a management consulting company.

Industry/Entity Type

Consulting

Font styles to use
Serif
Sans Serif

Requirements
Must have
• Slides that are common for consulting companies.
The ability to use the deck as a report - not just a presentation format

```html
<!DOCTYPE html>
<html lang="en">
<head>
<meta charset="utf-8">
<title>Calder Partners – Deck Template</title>
<link href="https://fonts.googleapis.com/css2?family=Montserrat:wght@400;500;700;800&family=Lato:wght@400&family=Roboto:wght@300&display=swap" rel="stylesheet">
<style>
:root{
  --board:#a3a3a3;
  --white:#ffffff;
  --ink:#111111;
  --body:#6b707a;
  --teal:#6aaea3;
  --teal-bright:#3fb0a0;
  --teal-deep:#1f4f49;
  --navy:#0f1f44;
  --axis:#cfcfcf;
}
*{margin:0;padding:0;box-sizing:border-box}
html,body{width:1200px;height:1072px;overflow:hidden}
body{background:radial-gradient(ellipse at center,#b8b8b8 0%,var(--board) 80%);position:relative;font-family:'Lato',sans-serif}
.slide{position:absolute;width:539px;height:303px;background:var(--white);overflow:hidden;box-shadow:0 10px 30px rgba(0,0,0,.35)}
.col-left{left:50px}.col-right{left:611px}
.row-1{top:50px}.row-2{top:385px}.row-3{top:719px}
.brand-name{position:absolute;font-family:'Montserrat',sans-serif;font-weight:700;color:var(--ink);white-space:nowrap}
.brand-name.small{top:22px;right:20px;font-size:11px;letter-spacing:.3px}
.brand-name.light{color:var(--white)}
.slide-title{position:absolute;left:19px;top:14px;font-family:'Montserrat',sans-serif;font-weight:800;font-size:23px;color:var(--ink);letter-spacing:.2px}
.photo{position:absolute}
/* cover */
.cover .photo{inset:0;background:linear-gradient(180deg,#0a0a0a 0%,#2a2a2a 40%,#8c8c8c 62%,#3a3a3a 80%,#111 100%)}
.cover .brand-name{top:42px;left:0;right:0;text-align:center;color:var(--white);font-size:26px;letter-spacing:.5px}
/* team */
.team .photo{inset:0;background:linear-gradient(120deg,#1f3a78 0%,#34589e 45%,#24437f 100%)}
.team-band{position:absolute;left:0;top:175px;width:354px;height:58px;background:var(--teal-bright);display:flex;align-items:center;padding-left:37px}
.team-band h2{font-family:'Montserrat',sans-serif;font-weight:800;font-size:23px;color:var(--white);letter-spacing:.2px}
/* process */
.process-copy{position:absolute;left:20px;top:64px;width:245px;font-size:8.6px;line-height:16px;color:var(--body)}
.process .photo{left:298px;top:64px;width:228px;height:227px;background:linear-gradient(180deg,#dfe9f8 0%,#b9dcef 60%,#a7d3ea 100%)}
.partner{position:absolute;display:flex;align-items:center;gap:6px;font-family:'Montserrat',sans-serif}
.partner.proxy{top:238px;left:55px;font-size:7.5px;letter-spacing:1.2px;color:var(--ink);font-weight:500}
.partner.proxy .mark{width:9px;height:9px;border-radius:50%;background:#e2522a}
.partner.paint{top:262px;left:20px;font-size:17px;font-weight:800;color:var(--navy)}
.partner.paint .mark{width:12px;height:12px;background:var(--navy)}
/* chart */
.chart{position:absolute;left:0;top:0}
.chart text{font-family:'Roboto',sans-serif;font-weight:300;fill:#333}
.chart .legend-text{font-family:'Montserrat',sans-serif;font-weight:700;fill:var(--white);font-size:9.5px}
/* offer */
.offer-item{position:absolute;width:225px}
.offer-num{font-family:'Montserrat',sans-serif;font-weight:400;font-size:26px;color:var(--teal);line-height:1}
.offer-head{margin-top:11px;font-family:'Montserrat',sans-serif;font-size:9.5px;color:var(--ink);font-weight:400}
.offer-text{margin-top:9px;font-size:6.6px;line-height:13.2px;color:var(--body)}
/* thanks */
.thanks{background:var(--teal)}
.thanks h2{position:absolute;left:0;right:0;top:112px;text-align:center;font-family:'Montserrat',sans-serif;font-weight:800;font-size:66px;color:var(--white);letter-spacing:-1px}
.thanks .photo{left:369px;top:186px;width:170px;height:117px;background:radial-gradient(ellipse at 70% 60%,#2f6d65 0%,var(--teal-deep) 60%,rgba(31,79,73,0) 100%)}
</style>
</head>
<body>

<section class="slide cover col-left row-1">
  <div class="photo" role="img" aria-label="Black and white city skyline at night"></div>
  <div class="brand-name">Calder Partners</div>
</section>

<section class="slide team col-right row-1">
  <div class="photo" role="img" aria-label="Colleagues meeting in an office, blue toned photograph"></div>
  <div class="brand-name small light">Calder Partners</div>
  <div class="team-band"><h2>A TEAM YOU CAN TRUST</h2></div>
</section>

<section class="slide process col-left row-2">
  <h1 class="slide-title">PROCESS DISCLOSURE</h1>
  <div class="brand-name small">Calder Partners</div>
  <p class="process-copy">Lorem ipsum dolor sit amet, consectetur adipiscined do eiusmod tempor incididunt ut labore et dolore magna alm suspendisse ultrices gravisus commodo vivecenas accumsan lacusacilisis. Lorem ipsum dolor sit ansectetur adipiscing elit, sed do eiusmod tempor incididunt ut labore et dolore magna aliq ips suspendisse ultrices gravisus commodo vivecenas accumsan lacus vacilisis. Lorem ipsum dolor sit amet, consectetur adipiscing elit, sed do eiusmod tempor incididunt ut labore et dolore magna aliq ipsum suspendisavisus commodo vivecenas accumsan</p>
  <div class="partner proxy"><span class="mark"></span>ALDINE PROXY</div>
  <div class="partner paint">Brightcoat Group<span class="mark"></span></div>
  <div class="photo" role="img" aria-label="Statue with raised torch against a pale blue sky"></div>
</section>

<section class="slide esg col-right row-2">
  <h1 class="slide-title">ESG INFLUENCE</h1>
  <div class="brand-name small">Calder Partners</div>
  <svg class="chart" width="539" height="303" viewBox="0 0 539 303">
    <g font-size="8" text-anchor="end">
      <text x="51" y="272">0%</text><text x="51" y="254">5%</text><text x="51" y="236">10%</text>
      <text x="51" y="218">15%</text><text x="51" y="200">20%</text><text x="51" y="182">25%</text>
      <text x="51" y="164">30%</text><text x="51" y="147">35%</text><text x="51" y="129">40%</text>
      <text x="51" y="111">45%</text><text x="51" y="93">50%</text>
    </g>
    <line x1="60" y1="269" x2="500" y2="269" stroke="var(--axis)" stroke-width="1"/>
    <rect x="186" y="82" width="167" height="22" fill="var(--navy)"/>
    <text class="legend-text" x="269.5" y="96.5" text-anchor="middle">ESG INFLUENCE OF INVESTORS</text>
    <g fill="var(--teal)">
      <rect x="78" y="248" width="18" height="21"/>
      <rect x="133" y="140" width="18" height="129"/>
      <rect x="188" y="205" width="18" height="64"/>
      <rect x="243" y="220" width="18" height="49"/>
      <rect x="298" y="177" width="18" height="92"/>
      <rect x="353" y="223" width="18" height="46"/>
      <rect x="409" y="170" width="18" height="99"/>
      <rect x="463" y="101" width="18" height="168"/>
    </g>
    <g font-size="8" text-anchor="middle">
      <text x="87" y="243">5.94%</text><text x="142" y="135">35.97%</text><text x="197" y="200">17.93%</text>
      <text x="252" y="215">13.70%</text><text x="307" y="172">25.75%</text><text x="362" y="218">12.78%</text>
      <text x="418" y="165">27.60%</text><text x="472" y="96">46.83%</text>
    </g>
    <g font-size="8" text-anchor="middle">
      <text x="87" y="283">Kovar</text><text x="142" y="283">Lumen Signatory</text><text x="197" y="283">Qestra</text>
      <text x="252" y="283">Tallis Member</text><text x="307" y="283">Sustainwise</text><text x="362" y="283">Verdan</text>
      <text x="418" y="283">Ostrel</text><text x="472" y="283">Halden Pact</text>
    </g>
  </svg>
</section>

<section class="slide offer col-left row-3">
  <h1 class="slide-title">WHAT WE OFFER</h1>
  <div class="brand-name small">Calder Partners</div>
  <div class="offer-item" style="left:18px;top:60px">
    <div class="offer-num">01</div>
    <div class="offer-head">1.234 LOREM IPSUM</div>
    <p class="offer-text">Lorem ipsum dolor sit amet, consectetur adipiscined do eiusmod tempor incididunt ut labore et dolore magna alm suspendisse ultrices gravisuscom modo vivecenas accumsanLorem ipsum dolor sit ansectetur adipiscing elit, sed do eiusmod tempor incididunt ut labore et dolore magna</p>
  </div>
  <div class="offer-item" style="left:283px;top:60px">
    <div class="offer-num">02</div>
    <div class="offer-head">40% LOREM IPSUM</div>
    <p class="offer-text">Lorem ipsum dolor sit amet, consectetur adipiscined do eiusmod tempor incididunt ut labore et dolore magna alm suspendisse ultrices gravisuscom modo vivecenas accumsanLorem ipsum dolor sit ansectetur adipiscing elit, sed do eiusmod tempor incididunt ut labore et dolore magna</p>
  </div>
  <div class="offer-item" style="left:18px;top:183px">
    <div class="offer-num">03</div>
    <div class="offer-head">10mln LOREM IPSUM</div>
    <p class="offer-text">Lorem ipsum dolor sit amet, consectetur adipiscined do eiusmod tempor incididunt ut labore et dolore magna alm suspendisse ultrices gravisuscom modo vivecenas accumsanLorem ipsum dolor sit ansectetur adipiscing elit, sed do eiusmod tempor incididunt ut labore et dolore magna</p>
  </div>
  <div class="offer-item" style="left:283px;top:183px">
    <div class="offer-num">04</div>
    <div class="offer-head">200 LOREM IPSUM</div>
    <p class="offer-text">Lorem ipsum dolor sit amet, consectetur adipiscined do eiusmod tempor incididunt ut labore et dolore magna alm suspendisse ultrices gravisuscom modo vivecenas accumsanLorem ipsum dolor sit ansectetur adipiscing elit, sed do eiusmod tempor incididunt ut labore et dolore magna</p>
  </div>
</section>

<section class="slide thanks col-right row-3">
  <div class="brand-name small">Calder Partners</div>
  <h2>THANK YOU</h2>
  <div class="photo" role="img" aria-label="Roaring stone lion sculpture in dark teal tones"></div>
</section>

</body>
</html>
```